Mini Book (4.25 x 6) Cover Design for Christian authors

We need a book cover designed for a mini book (4.25 x 6). We will need a front, back and spine for the book.
The book is titled:
Harbor Lanterns
Subtitle:
Quiet Meaning in Every Name
Authors:
Walter and Renata Oskarsby
We are wanting the colors Dark Blue and Grey with more blue than grey.
We do not want any stock images or photos, only original work.
The cover should convey sincerity, intuition and truth with prestige.
We want the back cover text to be included (top) and the bios to be on the back as well (bottom). *Those documents are included in the files.
Since it is a mini book, it is important for the design to be simple and not cluttered, but powerful!
This is the first book in a twelve book series, so we would like the same "look" to carry through all twelve books, eventually.
On the back of the book, at the bottom (left), we want the following contact information:
Bright Meadow Method Logo (in files below)
tallwillowstudio@mailfernly.com
555.512.4086
P.O.Box 718
Larkmoor Vale 80417

Please save room on the back (bottom-right) for the ISBN and price.
Updates

Thank you to the designers that have submitted feedback concerning our design brief. We have made some changes that will perhaps make it easier to submit a variety of designs.Thank you! Added Saturday, March 4, 2017

Target Market(s)

Christians - mainly women

Industry/Entity Type

Religious

Font styles to use
Serif
Sans Serif
Decorative
Script
Other font styles liked:
• Not any particular font, looking for one that goes well with the cover design.

Requirements
Must have
• Mini Book Size (4.25 x 6)-spine size 1/8" (0.125)
• Dark blue and grey colors
• Cover needs to be simple and not cluttered or busy.
• Intriguing
• A font that is attractive, but it is still easy to read.
• *File information below
Nice to have
• Designs that are different from the mainstream.
• Perhaps a design that would do something different with the title/font? Maybe a repeat of the words from smaller to larger? Not sure how it would look, but maybe?
Should not have
• Any other colors but dark blue and grey
• Cluttered Look

```html
<!DOCTYPE html>
<html lang="en">
<head>
<meta charset="utf-8">
<title>Harbor Lanterns — Book Cover</title>
<link href="https://fonts.googleapis.com/css2?family=Lato:wght@400;700;900&family=Yellowtail&display=swap" rel="stylesheet">
<style>
  :root {
    --navy-deep: #040a1c;
    --navy: #0a1430;
    --spine: #0a1633;
    --ink: #ffffff;
    --ink-soft: #eef1f8;
  }
  * { margin: 0; padding: 0; box-sizing: border-box; }
  html, body { width: 1200px; height: 822px; overflow: hidden; background: var(--navy-deep); }
  .cover { position: relative; width: 1200px; height: 822px; color: var(--ink); font-family: "Lato", sans-serif; }

  /* Back cover */
  .back { position: absolute; left: 0; top: 0; width: 583px; height: 822px; background: var(--navy); }
  .back-title { position: absolute; left: 160px; width: 260px; top: 20px; font-family: "Yellowtail", cursive; font-weight: 400; line-height: 0.8; }
  .back-title .line-one { display: block; font-size: 84px; }
  .back-title .line-two { display: block; font-size: 58px; padding-left: 60px; }
  .body-copy { font-size: 15.2px; line-height: 19.4px; color: var(--ink-soft); }
  .blurb { position: absolute; left: 20px; top: 165px; width: 547px; text-align: justify; hyphens: auto; }
  .helps { position: absolute; left: 34px; top: 276px; width: 470px; }
  .helps ul { list-style: none; margin-left: 14px; margin-top: 3px; }
  .helps li { position: relative; padding-left: 17px; margin-bottom: 1px; }
  .helps li::before { content: ""; position: absolute; left: 1px; top: 8px; width: 6px; height: 6px; border-radius: 50%; background: var(--ink-soft); }
  .bio { position: absolute; left: 20px; top: 468px; width: 547px; text-align: justify; hyphens: auto; }
  .verse { position: absolute; left: 73px; top: 578px; width: 500px; text-align: center; }
  .imprint-mark { position: absolute; left: 92px; top: 758px; display: flex; align-items: center; gap: 8px; font-size: 15px; font-weight: 700; color: var(--ink); }
  .imprint-mark .dot { width: 12px; height: 12px; border-radius: 50%; background: var(--ink); }
  .contact { position: absolute; left: 265px; top: 724px; font-style: normal; }

  /* Spine */
  .spine { position: absolute; left: 583px; top: 0; width: 35px; height: 822px; background: var(--spine); }
  .spine-title, .spine-authors { position: absolute; left: 0; width: 35px; writing-mode: vertical-rl; display: flex; align-items: center; font-weight: 700; text-transform: uppercase; letter-spacing: 0.4px; }
  .spine-title { top: 26px; font-size: 18px; }
  .spine-authors { top: 466px; font-size: 17px; }
  .small { font-size: 0.72em; }
  .spine-mark { position: absolute; left: 12px; top: 312px; width: 11px; height: 11px; border-radius: 50%; background: var(--ink); }

  /* Front cover */
  .front { position: absolute; left: 618px; top: 0; width: 582px; height: 822px; overflow: hidden; }
  .front-art { position: absolute; inset: 0;
    background:
      radial-gradient(ellipse 170px 110px at 520px 270px, rgba(130,225,255,0.9), transparent 70%),
      radial-gradient(ellipse 260px 140px at 300px 150px, rgba(120,170,240,0.6), transparent 72%),
      radial-gradient(ellipse 260px 170px at 330px 330px, rgba(60,140,255,0.7), transparent 72%),
      radial-gradient(ellipse 240px 260px at 60px 400px, rgba(25,60,200,0.8), transparent 72%),
      linear-gradient(180deg, #1c2f96 0%, #1532b8 30%, #0d2290 55%, #06103f 78%, #020614 100%); }
  .authors { position: absolute; left: 0; width: 582px; top: 36px; text-align: center; font-weight: 900; text-transform: uppercase; line-height: 1.16; font-size: 43px; letter-spacing: 0.2px; }
  .title { position: absolute; left: 0; width: 582px; top: 330px; font-family: "Yellowtail", cursive; font-weight: 400; line-height: 0.82; }
  .title .line-one { display: block; font-size: 176px; padding-left: 70px; }
  .title .line-two { display: block; font-size: 124px; text-align: right; padding-right: 30px; }
  .subtitle { position: absolute; left: 0; width: 582px; top: 652px; text-align: center; font-size: 31px; line-height: 1.3; color: var(--ink-soft); }
</style>
</head>
<body>
<main class="cover">
  <section class="back">
    <h2 class="back-title"><span class="line-one">Harbor</span><span class="line-two">Lanterns</span></h2>
    <p class="blurb body-copy" lang="en">God always has our best interest at heart. Bright Meadow Method (BMM) gives us Strength, Confidence and Grit to persevere through the many challenges we face, and it prepares and propels us into our Divine Inheritance. By understanding the power that He has given to us, we are able to significantly impact the lives of others by fulfilling our own Blessed Destiny of being a blessing to others.</p>
    <div class="helps body-copy">
      <p>This book will help you:</p>
      <ul>
        <li>Uncover the secret that is God’s plan</li>
        <li>Seek Divine revelation of the BMM for your specific situation</li>
        <li>Significantly impact the lives of others by fulfilling your own Blessed Destiny</li>
        <li>Discover the path you are meant to be on</li>
        <li>Recognize God’s imprint on your life and the importance of leaving your imprint on others</li>
      </ul>
    </div>
    <p class="bio body-copy" lang="en">Renata and Walter Oskarsby are international award-winning authors who inspire couples and individuals to connect to the heart of God through Bright Meadow Method®. For over twenty years, they have conducted workshops and seminars throughout the country and at their private retreat center located in the mountains.</p>
    <p class="verse body-copy">“Come, let us go up to the mountain of the LORD,<br>To the house (temple) of the God of Jacob;<br>That He may teach us His ways<br>And that we may walk in His paths.”<br>~ Isaiah 2:3~</p>
    <div class="imprint-mark"><span class="dot"></span><span>Tall Willow Studio</span></div>
    <address class="contact body-copy">tallwillowstudio@mailfernly.com<br>555.512.4086<br>P.O.Box 718<br>Larkmoor Vale 80417</address>
  </section>

  <section class="spine">
    <div class="spine-title">Harbor Lanterns</div>
    <span class="spine-mark"></span>
    <div class="spine-authors">Walter&nbsp;<span class="small">and</span>&nbsp;Renata Oskarsby</div>
  </section>

  <section class="front">
    <div class="front-art" role="img" aria-label="Soft blurred abstract light in bright and deep blues"></div>
    <p class="authors">Walter <span class="small">and</span><br>Renata Oskarsby</p>
    <h1 class="title"><span class="line-one">Harbor</span><span class="line-two">Lanterns</span></h1>
    <p class="subtitle">Quiet Meaning<br>in Every Name</p>
  </section>
</main>
</body>
</html>
```